Business Cards and label design needed!

I am a metalsmith, working in sterling silver, brass and moving slowly into adding some gold accent pieces. I also use patinas to add color to brass pieces. The peacock feather is used in my packaging, as both a label and tissue paper. I am attaching what I am currently using, and printing at home, but I need a design that I can have professionally printed. My website is www.willowharborcrafts.com
Target Market(s)
Established Professionals, Independent thinkers, Art donors, Artist supporters
Industry/Entity Type
Jewelry
Contact Information for Business Card
I would like a business card with the basic contact information, including Facebook and Instagram. I currently use a peacock feather and would like to continue that. I like to use turquoise, Tiffany blue and colors in that direction. I am open to other suggestions. I would like to be able to transfer the design to oval labels as well.
Font styles to use
Other font styles liked:
- Garamond or other fonts that have a slight script that is easy to read
Look and feel

```html
<!DOCTYPE html>
<html lang="en">
<head>
<meta charset="utf-8">
<title>Willow Harbor Crafts – Business Card</title>
<link href="https://fonts.googleapis.com/css2?family=Roboto:wght@400;500&display=swap" rel="stylesheet">
<style>
  :root {
    --backdrop: #2e2e30;
    --paper: #f3f3f2;
    --teal: #15949a;
    --indigo: #1f2a8e;
    --ink: #4a4a4a;
    --rule: #c9c9c9;
    --white: #ffffff;
    --glow-light: rgba(95, 199, 196, 0.75);
    --glow-mid: rgba(27, 127, 147, 0.45);
    --glow-clear: rgba(31, 42, 142, 0);
  }
  * { box-sizing: border-box; margin: 0; padding: 0; }
  html, body { width: 1200px; height: 960px; overflow: hidden; }
  body {
    background: var(--backdrop);
    position: relative;
    font-family: "Roboto", Arial, sans-serif;
  }
  .card {
    position: absolute;
    width: 600px;
    height: 343px;
    overflow: hidden;
  }
  /* Front */
  .card-front { left: 322px; top: 108px; background: var(--paper); }
  .brand-name {
    position: absolute;
    left: 20px; width: 268px; top: 148px;
    text-align: center;
    font-size: 24px;
    font-weight: 400;
    color: var(--indigo);
  }
  .divider {
    position: absolute;
    left: 288px; top: 107px;
    width: 1px; height: 130px;
    background: var(--rule);
  }
  .contact { position: absolute; left: 311px; top: 112px; color: var(--ink); }
  .contact-name {
    font-size: 21px; font-weight: 500; color: var(--teal);
    letter-spacing: 0.2px; line-height: 26px;
  }
  .contact-address { font-size: 15px; margin-top: 6px; line-height: 20px; }
  .contact-list { list-style: none; margin-top: 8px; }
  .contact-list li {
    display: flex; align-items: center; gap: 8px;
    font-size: 15px; line-height: 19px;
  }
  .contact-list svg { width: 13px; height: 13px; fill: var(--teal); flex: none; }
  .band { position: absolute; bottom: 0; left: 0; width: 600px; height: 13px; }
  /* Back */
  .card-back { left: 320px; top: 493px; background: var(--indigo); }
  .feather-art {
    position: absolute; inset: 0;
    background: radial-gradient(ellipse 190px 200px at 36% 42%, var(--glow-light) 0%, var(--glow-mid) 45%, var(--glow-clear) 100%);
  }
  .back-name {
    position: absolute; right: 32px; top: 254px;
    font-size: 32px; font-weight: 400; color: var(--white);
  }
  .back-url {
    position: absolute; right: 28px; top: 302px;
    font-size: 15px; letter-spacing: 3.8px; color: var(--white);
  }
</style>
</head>
<body>
  <section class="card card-front">
    <div class="brand-name">Willow Harbor Crafts</div>
    <div class="divider"></div>
    <div class="contact">
      <div class="contact-name">MARLA QUINN</div>
      <div class="contact-address">Brookhaven, TX 76411</div>
      <ul class="contact-list">
        <li>
          <svg viewBox="0 0 16 16" aria-hidden="true"><path d="M3.5 1l2.5 3-1.5 2c.8 1.8 2.2 3.2 4 4l2-1.5 3 2.5-1.5 2.5C6.5 15 1 9.5 1 2.5z"/></svg>
          555-014-2297
        </li>
        <li>
          <svg viewBox="0 0 16 16" aria-hidden="true"><path d="M1 3h14L8 8.5z M1 4.5l7 5.5 7-5.5V13H1z"/></svg>
          studio@willowharborcrafts.com
        </li>
        <li>
          <svg viewBox="0 0 16 16" aria-hidden="true"><circle cx="8" cy="8" r="7"/><path d="M4 4.5c1.5 0 2 1 3 1.5s0 2-1 2.5S5 11 4 11M10 3c-.5 1.5 1 2 2 2.5M9 9.5c1 0 2 .5 2 2" stroke="#f3f3f2" stroke-width="1.2" fill="none"/></svg>
          www.willowharborcrafts.com
        </li>
      </ul>
    </div>
    <svg class="band" viewBox="0 0 600 13" aria-hidden="true">
      <rect x="0" y="0" width="600" height="13" fill="var(--teal)"/>
      <polygon points="394,0 600,0 600,13 390,13" fill="var(--indigo)"/>
      <polygon points="390,0 394,0 390,13 386,13" fill="#ffffff"/>
    </svg>
  </section>

  <section class="card card-back">
    <div class="feather-art" role="img" aria-label="Peacock feather illustration"></div>
    <div class="back-name">Willow Harbor Crafts</div>
    <div class="back-url">www.willowharborcrafts.com</div>
  </section>
</body>
</html>
```